Redesign Of Flower Delivery Subscription Service Website

I need a revamped website of www.petal-rush.com

Please revamp current design using same content....

Target Market(s)

people who buy flowers. Brides, wedding planners, wedding photographer, married man, boyfriend, etc.

Industry/Entity Type

Florist

Number of Pages Required

5+ page

Colors

Designer to choose colors to be used in the design.

Requirements
Must have
• I need a revamped website of www.petal-rush.com
• Please revamp current design using same content....
Nice to have
Should not have

```html
<!DOCTYPE html>
<html lang="en">
<head>
<meta charset="utf-8">
<title>PetalRush – Monthly Flower Delivery</title>
<link rel="stylesheet" href="https://fonts.googleapis.com/css2?family=Raleway:wght@300;400;500;600;700&family=Great+Vibes&family=Dancing+Script:wght@500&family=Abel&display=swap">
<style>
:root{
  --green:#8fd14f;
  --green-dark:#7cc040;
  --green-light:#b3e07f;
  --orange:#f7a823;
  --ink:#222;
  --muted:#777;
  --topbar:#e4e4e4;
  --section-gray:#efeeee;
  --card:#e7e5e5;
  --footer:#3c3c3c;
  --footer-line:#666;
  --white:#fff;
}
*{box-sizing:border-box;margin:0;padding:0}
html,body{width:1200px;height:2727px;overflow:hidden}
body{position:relative;font-family:"Raleway",Arial,sans-serif;color:var(--ink);background:var(--white)}
.abs{position:absolute}

/* top bar */
.topbar{left:0;top:0;width:1200px;height:30px;background:var(--topbar);font-size:10px;color:#555;text-transform:uppercase;letter-spacing:.3px}
.topbar span{position:absolute;top:9px}

/* header */
.header{left:0;top:30px;width:1200px;height:94px;background:var(--white)}
.brand{position:absolute;left:73px;top:28px;font-size:32px;font-weight:500;color:var(--green-dark);letter-spacing:.5px}
.brand-dot{display:inline-block;width:12px;height:12px;background:var(--green-dark);border-radius:50%;margin-left:6px;vertical-align:6px}
.nav{position:absolute;left:413px;top:44px;display:flex;gap:15px;font-size:11.5px;text-transform:uppercase;color:#666}
.nav .active{color:var(--green-dark)}

/* hero */
.hero{left:0;top:124px;width:1200px;height:558px;background:linear-gradient(90deg,#f6f6f6 0%,#f1f1f1 45%,#ece7ea 60%,#e8c6d3 100%)}
.hero-photo{position:absolute;right:0;top:0;width:640px;height:558px;background:radial-gradient(ellipse at 65% 55%,#f08fb1 0%,#f2a9c4 35%,#e9cfd9 65%,rgba(240,236,238,0) 85%)}
.hero-title{position:absolute;left:88px;top:150px;font-family:"Great Vibes",cursive;font-size:104px;color:var(--green);line-height:1}
.hero-sub{position:absolute;left:87px;top:272px;font-size:23px;color:#333}
.hero-price{position:absolute;left:86px;top:300px;font-size:30px;color:#333}
.hero-tag{position:absolute;top:363px;height:35px;background:var(--green);color:var(--white);font-size:14px;text-align:center;line-height:35px;border-radius:2px}

/* signup band */
.signup{left:0;top:682px;width:1200px;height:107px;background:var(--green)}
.signup-text{position:absolute;left:203px;top:27px;font-family:"Abel",sans-serif;color:var(--white);font-size:23px;line-height:1.2}
.signup-text strong{font-size:26px;font-weight:700}
.signup-input{position:absolute;left:557px;top:31px;width:406px;height:38px;background:var(--green-light);border:1px solid #c8eaa3;color:var(--white);font-size:9px;padding:12px 14px}
.signup-btn{position:absolute;left:978px;top:31px;width:74px;height:38px;background:var(--orange);color:var(--white);font-size:9px;text-align:center;line-height:38px}

/* feature cards */
.features{left:0;top:789px;width:1200px;height:675px;background:var(--section-gray)}
.card{position:absolute;top:71px;width:344px;height:540px;background:var(--card)}
.card-photo{height:271px;display:flex;align-items:center;justify-content:center;text-align:center;color:var(--white);font-size:30px;font-weight:300;line-height:1.2;text-transform:uppercase}
.card-body{padding:26px 24px;text-align:center;font-size:17.5px;line-height:1.3;color:#333}
.card-body p+p{margin-top:20px}
.card-body b{font-weight:600;color:#111}

/* subscription */
.subscription{left:0;top:1464px;width:1200px;height:796px;background:radial-gradient(ellipse at 50% 55%,#d7bcc4 0%,#cfd5c7 35%,#e4e4e2 70%,#efefef 100%)}
.sub-title{position:absolute;left:0;width:1200px;top:96px;text-align:center;font-family:"Dancing Script",cursive;font-size:74px;color:#111}
.sub-heading{position:absolute;left:0;width:1200px;top:186px;text-align:center;font-size:33px;font-weight:500;color:#111}
.bubble{position:absolute;top:327px;width:320px;height:320px;border-radius:50%;border:6px solid var(--white);display:flex;align-items:center;justify-content:center;text-align:center;padding:0 40px;color:var(--white);font-size:28px;font-weight:500;line-height:1.18}

/* footer */
.footer-rule{left:0;top:2260px;width:1200px;height:4px;background:var(--orange)}
.footer{left:0;top:2264px;width:1200px;height:405px;background:var(--footer);color:#ddd}
.footer h4{position:absolute;top:47px;font-size:16px;font-weight:700;color:var(--white);letter-spacing:.3px}
.services{position:absolute;left:120px;top:97px;list-style:none;font-size:13.5px;color:#ccc;line-height:23px}
.services li::before{content:">";margin-right:10px}
.contact-item{position:absolute;left:378px;font-size:13.5px;color:#ddd;display:flex;gap:12px}
.contact-item b{font-weight:600;color:var(--white)}
.contact-item small{display:block;font-size:12.5px;color:#bbb;line-height:17px}
.quote-note{position:absolute;left:689px;top:94px;font-size:11.5px;color:#ccc}
.field{position:absolute;border:1px solid #8a8a8a;font-size:11px;color:#ddd;padding:10px 12px}
.quote-btn{position:absolute;left:686px;top:306px;width:204px;height:38px;background:var(--green);color:var(--white);font-weight:700;font-size:15px;padding:10px 14px}

.bottombar{left:0;top:2669px;width:1200px;height:58px;background:var(--green)}
.copyright{position:absolute;left:130px;top:22px;font-size:11.5px;color:#222}
.social{position:absolute;left:976px;top:18px;display:flex;gap:5px}
.social span{width:23px;height:23px;border-radius:50%;background:#111}
</style>
</head>
<body>

<div class="abs topbar">
  <span style="left:78px">A special gift for your first order</span>
  <span style="left:478px;color:#222">Make a call us +45 000 1234</span>
  <span style="left:848px">Login / Register / MyAccount</span>
  <span style="left:1084px">Help</span>
</div>

<header class="abs header">
  <div class="brand">PetalRush<span class="brand-dot"></span></div>
  <nav class="nav">
    <span class="active">Home</span><span>How it works</span><span>Delivery areas</span><span>Franchise</span><span>Blog</span><span>Free flowers monthly</span><span>Corporate arrangements</span>
  </nav>
</header>

<section class="abs hero">
  <div class="hero-photo" role="img" aria-label="Bouquet of pink ranunculus flowers"></div>
  <h1 class="hero-title">Always fresh</h1>
  <p class="hero-sub">Beautiful Flower Arrangements Delivered Monthly</p>
  <p class="hero-price">Now only $69,95/MTH ($100 value)</p>
  <span class="hero-tag" style="left:153px;width:107px">Free wash</span>
  <span class="hero-tag" style="left:280px;width:107px">Free Delivery</span>
  <span class="hero-tag" style="left:405px;width:106px">Free upgrade</span>
</section>

<section class="abs signup">
  <p class="signup-text">Enter Your Email To<br><strong>Receive A Free Upgrade</strong></p>
  <div class="signup-input">Your Email Address</div>
  <div class="signup-btn">Submit</div>
</section>

<section class="abs features">
  <article class="card" style="left:69px">
    <div class="card-photo" role="img" aria-label="Florist holding a sunflower bouquet in a flower shop" style="background:linear-gradient(135deg,#5a4a35,#8a7450 50%,#4d3e2c)">Set it and<br>forget it</div>
    <div class="card-body">
      <p>PetalRush is a "SET IT and FORGET IT" subscription based flower delivery service.</p>
      <p>For an Amazing price PetalRush will hand deliver a gorgeous arrangement directly to anyone you want every month without you having to worry about it.</p>
    </div>
  </article>
  <article class="card" style="left:425px">
    <div class="card-photo" role="img" aria-label="Close-up of purple and lilac flowers" style="background:linear-gradient(135deg,#6d58a8,#8b74c2 50%,#5a4794)">But never<br>forget again</div>
    <div class="card-body">
      <p>When setting up your account, you can choose exact delivery dates for the months that have special days such as <b>your Anniversary, Birthday, Valentines Day and Mothers Day.</b></p>
      <p>You might forget but we won't, we have got ya covered!</p>
    </div>
  </article>
  <article class="card" style="left:780px">
    <div class="card-photo" role="img" aria-label="Smiling florist in a shop holding a basket of flowers" style="background:linear-gradient(135deg,#6a5545,#94745e 50%,#5b4536)">Making someone's<br>day better</div>
    <div class="card-body">
      <p>Be the hero in that special someone's life each and every month.</p>
      <p><b>It feels good to make a difference in your loved ones day.</b></p>
    </div>
  </article>
</section>

<section class="abs subscription" role="img" aria-label="Faded photo of a colourful mixed bouquet in a white vase">
  <h2 class="sub-title">Monthly Subscription</h2>
  <p class="sub-heading">Based Flower Delivery Service in San Diego – CA by Our Florist Shop</p>
  <div class="bubble" role="img" aria-label="Pink roses" style="left:110px;background:radial-gradient(circle,#9a4a63,#6e2e44)">Exotic Flowers Garnished With Special Hues To Compliment Your Loved Ones</div>
  <div class="bubble" role="img" aria-label="Red and pink rose arrangement" style="left:449px;background:radial-gradient(circle,#8a3a3c,#4f2a2e)">Standard And Personalized Flower Arrangements For Special Occasions</div>
  <div class="bubble" role="img" aria-label="Orange autumn flowers" style="left:793px;background:radial-gradient(circle,#9a5a2a,#4d3420)">Get Yourself Subscribed And Claim Discounts On Big Orders!</div>
</section>

<div class="abs footer-rule"></div>
<footer class="abs footer">
  <h4 style="left:120px">MORE SERVICES</h4>
  <ul class="services">
    <li>Corporate Arrangements</li><li>Hotel Arrangements</li><li>Events</li><li>Weddings</li>
  </ul>

  <h4 style="left:378px">CONTACT US</h4>
  <div class="contact-item" style="top:105px">
    <svg width="12" height="16" viewBox="0 0 12 16"><path d="M6 0a6 6 0 0 0-6 6c0 4.5 6 10 6 10s6-5.5 6-10a6 6 0 0 0-6-6z" fill="#fff"/><circle cx="6" cy="6" r="2.2" fill="#3c3c3c"/></svg>
    <div><b>Address</b><small>1480 Harbor Lane,<br>San Diego CA 92101</small></div>
  </div>
  <div class="contact-item" style="top:170px">
    <svg width="13" height="13" viewBox="0 0 24 24"><path d="M6.6 10.8a15.1 15.1 0 0 0 6.6 6.6l2.2-2.2a1 1 0 0 1 1-.25 11.4 11.4 0 0 0 3.6.57 1 1 0 0 1 1 1V20a1 1 0 0 1-1 1A17 17 0 0 1 3 4a1 1 0 0 1 1-1h3.5a1 1 0 0 1 1 1c0 1.25.2 2.45.57 3.57a1 1 0 0 1-.25 1z" fill="#fff"/></svg>
    <span>Phone : 619-555-0142</span>
  </div>
  <div class="contact-item" style="top:226px;font-size:12.5px">
    <svg width="13" height="10" viewBox="0 0 13 10"><rect width="13" height="10" rx="1" fill="#fff"/><path d="M0.5 0.8 6.5 5.5 12.5 0.8" stroke="#3c3c3c" stroke-width="1.2" fill="none"/></svg>
    <span>Email hello@petalrush-sd.com</span>
  </div>

  <h4 style="left:689px">GET A QUOTE</h4>
  <p class="quote-note">Alternatively you can fill in the following Contact form</p>
  <div class="field" style="left:686px;top:140px;width:419px;height:38px">Name</div>
  <div class="field" style="left:686px;top:188px;width:208px;height:38px">Phone No</div>
  <div class="field" style="left:898px;top:188px;width:207px;height:38px">your Email</div>
  <div class="field" style="left:686px;top:236px;width:419px;height:60px">Message</div>
  <div class="quote-btn">Submit</div>
</footer>

<div class="abs bottombar">
  <p class="copyright">© 2018 Company Name All Right Reserved</p>
  <div class="social"><span></span><span></span><span></span><span></span></div>
</div>

</body>
</html>
```